Header for Academic Handouts (How-to-Guides)

We are looking for a design element, which can be used as a visual header on A4-word-documents (Portrait-Set-Up). It shall be a graphic, visual language which is clearly understandable. The header height shall be between 0.75 - 1.5 inch – so it should not have too many small details. Attached below ideas/directions how the final document could look like.

The visual element shall symbolize by simple means the topic of “flipped classroom” or “active learning”. The documents with these new graphic elements will be used on handouts which are distributed in this training course:
https://www.korvanel.ch/en/the-korvanel-academy/education/educational-development/didaktische-weiterbildung/flipped-classroom.html

```html
<!DOCTYPE html>
<html lang="en">
<head>
<meta charset="utf-8">
<title>Flipped Classroom – Teaching Lab</title>
<link rel="stylesheet" href="https://fonts.googleapis.com/css2?family=Bebas+Neue&family=Carlito:wght@400;700&family=Fira+Sans+Condensed:wght@700&display=swap">
<style>
  :root {
    --sky: #4fb9ee;
    --mid-blue: #2f7fc0;
    --navy: #0c3c66;
    --ink: #111111;
    --paper: #ffffff;
    --edge: #9a9a9a;
    --bulb: #f2ea3a;
  }
  * { margin: 0; padding: 0; box-sizing: border-box; }
  html, body { width: 1200px; height: 1200px; overflow: hidden; background: var(--paper); }
  .canvas { position: relative; width: 1200px; height: 1200px; }
  .sheet {
    position: absolute; left: 188px; top: 0; width: 850px; height: 1200px;
    background: var(--paper); border-left: 1px solid var(--edge); border-right: 1px solid var(--edge);
    overflow: hidden;
    font-family: "Carlito", "Calibri", sans-serif; color: var(--ink);
    font-size: 14.6px; line-height: 20.5px;
  }
  .wave { position: absolute; left: 0; width: 850px; }
  .wave--top { top: 0; height: 140px; }
  .wave--bottom { bottom: 0; height: 60px; }
  .bulb-icon {
    position: absolute; left: 78px; top: 2px; width: 72px; height: 72px; border-radius: 50%;
    background: radial-gradient(circle, rgba(242,234,58,0.55), rgba(242,234,58,0));
  }
  .title {
    position: absolute; left: 84px; top: 8px; width: 436px; text-align: right;
    font-family: "Bebas Neue", "Oswald", sans-serif; color: var(--paper);
    font-size: 76px; line-height: 60px; letter-spacing: 0.5px;
  }
  .title span { display: block; }
  .title .line-2 { text-align: right; }
  .register {
    position: absolute; left: 500px; top: 24px; width: 345px; text-align: center;
    color: #eaf7ff; font-size: 17px; line-height: 24px;
  }
  .register strong { color: var(--paper); font-weight: 700; }
  .block { position: absolute; text-align: justify; }
  .block p + p { margin-top: 20.5px; }
  .indent { text-indent: 51px; }
  .heading {
    position: absolute; font-family: "Fira Sans Condensed", "Arial Narrow", sans-serif;
    font-weight: 700; font-size: 25px; line-height: 28px; letter-spacing: -0.3px; color: var(--ink);
  }
  .bullets { list-style: none; }
  .bullets li { position: relative; padding-left: 20px; margin-bottom: 20.5px; text-align: justify; }
  .bullets li::before {
    content: ""; position: absolute; left: 0; top: 6px; width: 9px; height: 9px;
    border-radius: 50%; background: var(--ink);
  }
  .plain-list p { margin-bottom: 20.5px; }
  .details p { margin-bottom: 20.5px; }
  .details b { font-weight: 700; }
</style>
</head>
<body>
<div class="canvas">
  <article class="sheet">
    <svg class="wave wave--top" viewBox="0 0 850 140" preserveAspectRatio="none" aria-hidden="true">
      <path d="M0,118 C160,150 300,152 470,136 C620,120 740,104 850,102 L850,140 L0,140 Z" fill="var(--navy)"/>
      <path d="M0,118 C160,142 300,144 470,128 C620,112 740,98 850,96 L850,112 C740,112 620,124 470,138 C300,150 160,146 0,124 Z" fill="var(--mid-blue)"/>
      <path d="M0,0 L850,0 L850,96 C740,98 620,108 470,122 C300,138 160,136 0,116 Z" fill="var(--sky)"/>
      <path d="M0,124 C160,148 300,152 470,138 C620,124 740,112 850,112 L850,140 L0,140 Z" fill="var(--paper)"/>
      <path d="M0,118 C160,144 300,148 470,132 C620,118 740,104 850,102 L850,134 C740,132 620,138 470,146 C300,156 160,150 0,124 Z" fill="var(--navy)"/>
    </svg>
    <div class="bulb-icon" role="img" aria-label="Light bulb idea icon"></div>
    <h1 class="title"><span class="line-1">Flipped</span><span class="line-2">Classroom</span></h1>
    <p class="register">To register, please send an email to<br><strong>Lena Hartwig</strong></p>

    <section class="block intro" style="left:75px; top:160px; width:330px;">
      <p class="indent">In the flipped classroom direct instruction moves to the individual learning space by taking the form of distance learning. Classroom lecture sessions are replaced with interactive problem-solving sequences where the teacher acts as a coach.</p>
      <p class="indent">In the Flipped Classroom Teaching Lab, participants flip their courses – or parts of courses – while receiving assistance and feedback during both planning and implementation.</p>
    </section>

    <h2 class="heading" style="left:54px; top:406px;">COURSE CONTENT</h2>
    <div class="block plain-list" style="left:91px; top:441px; width:310px; text-align:left;">
      <p>Develop a flipped classroom concept for your own teaching</p>
      <p>Pilot this project in Spring Semester&nbsp;&nbsp;&nbsp; 2017</p>
      <p>Review the project</p>
    </div>

    <h2 class="heading" style="left:55px; top:580px;">IS THIS COURSE FOR ME?</h2>
    <div class="block" style="left:77px; top:616px; width:323px;">
      <p class="indent">Our Teaching Labs are intended for experienced Korvanel teaching staff. We recommend that you have experience with.</p>
    </div>
    <ul class="block bullets" style="left:75px; top:695px; width:330px;">
      <li>Aligning learning objectives, learning activities and assessment.</li>
      <li>Using methods which actively engage students in learning.</li>
    </ul>

    <h2 class="heading" style="left:54px; top:812px;">DATES</h2>
    <ul class="block bullets" style="left:75px; top:846px; width:330px;">
      <li>Online preparation: 1-15 November 2016 (individual, minimum 1 hour)</li>
      <li>Opening workshop: 16 November 2016 (09:00-16:00)</li>
      <li>Individual preparation of pilot: 17 November 2016 – 19 February 2017</li>
      <li>Individual flipped classroom pilot: Spring Semester 2017</li>
      <li>Closing workshop (exchange of experiences): 22 March 2017 (09:00-16:00</li>
    </ul>

    <h2 class="heading" style="left:439px; top:152px;">OBJECTIVES</h2>
    <ul class="block bullets" style="left:442px; top:188px; width:355px;">
      <li>Select a flipped classroom variation suitable for your course.</li>
      <li>Apply methods appropriate to your new teaching role.</li>
      <li>Design teaching such that it provides continual feedback on learning progress towards clear, measurable goals, for both students and teachers.</li>
      <li>Align learning objectives, content, tasks and the final examination.</li>
      <li>Elaborate strategies to meet the particular challenges of flipped classroom teaching.</li>
    </ul>

    <h2 class="heading" style="left:439px; top:549px;">DETAILS</h2>
    <div class="block details" style="left:462px; top:580px; width:335px;">
      <p><b>Language</b>: English</p>
      <p><b>Cost</b>: Free of charge</p>
      <p style="text-align:left;"><b>Format</b>:<br>- Online independent study phase<br>- Two full-day workshops<br>- Individual pilot phase during the semester</p>
      <p><b>Workload</b>: 2 classroom days (each 09.00-16.00) + online independent study (individual, minimum 1 hr), individual preparation of flipped classroom teaching pilot during Spring Semester 2017</p>
      <p style="text-align:left;"><b>You will need</b>: Your own laptop or mobile device<br>Certificate: Certificate of attendance</p>
      <p>To receive a certificate of attendance, participants must attend workshop days 1 and 2 and pilot a flipped classroom in Spring Semester 2017.</p>
      <p>With your registration you agree to take part in the independent study phase and the two full-day workshops, and to pilot a flipped classroom in Spring Semester 2017.</p>
    </div>

    <svg class="wave wave--bottom" viewBox="0 0 850 60" preserveAspectRatio="none" aria-hidden="true">
      <path d="M0,10 C200,14 420,26 600,22 C720,19 800,12 850,14 L850,60 L0,60 Z" fill="var(--navy)"/>
      <path d="M0,20 C200,24 420,34 600,30 C720,27 800,22 850,24 L850,60 L0,60 Z" fill="var(--mid-blue)"/>
      <path d="M0,32 C200,36 420,44 600,40 C720,37 800,32 850,32 L850,60 L0,60 Z" fill="var(--sky)"/>
    </svg>
  </article>
</div>
</body>
</html>
```